Rock, Paper Scissors Championship Flyer

We need a dynamic, bold and exciting flyer to promote the following event at our sports center. The event will be primarily focused for adults, but children are welcome to join

Rock, Paper, Scissors Championship - $$$ prizes
Date: June 9th, 2018
Time: 11am-4pm
Fee: $2 to enter, free for spectators
Heats to determine the overall ‘Rock, Paper, Scissors’ champion!
- Cash prizes on offer
- Live music.
- Food and beverage available for purchase

Belmoray Sports Center, Roselle NJ
908-555-0163
www.belmoraypark.example

Must include our logo (does not have to be huge) and County seal (both attached)

Colors

Designer to choose colors to be used in the design.

Requirements
Must have
• Should be fun and colorful
• The following info and attached logos:
• Rock, Paper, Scissors Championship - $$$ prizes
• Date: June 9th, 2018
• Time: 11am-4pm
• Fee: $2 to enter, free for spectators
• Heats to determine the overall ‘Rock, Paper, Scissors’ champion!
• - Cash prizes on offer
• - Live music.
• - Food and beverage available for purchase
• Belmoray Sports Center, Roselle NJ
• 908-555-0163
• www.belmoraypark.example
Nice to have
• There are a few inspirational photos attached to give an idea of what we are looking for.

```html
<!DOCTYPE html>
<html lang="en">
<head>
<meta charset="utf-8">
<title>Rock Paper Scissors Championship Flyer</title>
<link rel="stylesheet" href="https://fonts.googleapis.com/css2?family=Luckiest+Guy&family=Fira+Sans+Condensed:wght@500;700;800&family=Bangers&display=swap">
<style>
  :root {
    --page-bg: #ececec;
    --sky-top: #2f86d6;
    --sky-mid: #7fbde8;
    --field-top: #7cc242;
    --field-bottom: #3c8f22;
    --rock-yellow: #ffd21f;
    --paper-white: #ffffff;
    --scissors-mint: #8fd4c4;
    --title-outline: #2b4a9a;
    --ribbon-blue: #3d5fb0;
    --ribbon-ink: #2b3f86;
    --band-green: rgba(180, 214, 60, 0.8);
    --heats-ink: #1f3a17;
    --bunting-pink: #ef86b6;
    --bunting-orange: #f39a2a;
    --bunting-teal: #5fc7c7;
    --seal-gold: #c9a65a;
  }
  * { box-sizing: border-box; margin: 0; padding: 0; }
  html, body { width: 1200px; height: 847px; overflow: hidden; background: var(--page-bg); }
  .canvas { position: relative; width: 1200px; height: 847px; }
  .flyer {
    position: absolute; left: 291px; top: 24px; width: 618px; height: 800px;
    overflow: hidden; box-shadow: 0 8px 24px rgba(0,0,0,.18);
  }
  .flyer-photo {
    position: absolute; inset: 0;
    background: linear-gradient(180deg, var(--sky-top) 0%, var(--sky-mid) 48%, #cfe6f2 56%, var(--field-top) 58%, var(--field-bottom) 100%);
  }
  .bunting {
    position: absolute; left: 0; right: 0; top: 0; height: 46px;
    background: linear-gradient(90deg, var(--bunting-pink), var(--bunting-orange), var(--bunting-teal), var(--bunting-pink), var(--bunting-orange), var(--bunting-teal));
    opacity: .85;
  }
  .club-mark {
    position: absolute; left: 30px; top: 78px; width: 120px;
    display: flex; flex-direction: column; align-items: center; gap: 6px;
    font-family: "Fira Sans Condensed", sans-serif; font-weight: 700;
    color: var(--paper-white); text-align: center; font-size: 15px; line-height: 1.1;
    text-transform: uppercase;
  }
  .club-dot { width: 30px; height: 30px; border-radius: 50%; background: var(--paper-white); }
  .county-seal {
    position: absolute; left: 52px; top: 176px; width: 76px; height: 76px;
    border-radius: 50%; background: var(--seal-gold); border: 3px solid #f5e6b8;
  }
  .title {
    position: absolute; left: 150px; top: 96px; width: 440px; text-align: center;
    font-family: "Luckiest Guy", "Bangers", sans-serif; font-weight: 400; line-height: .9;
    -webkit-text-stroke: 3px var(--title-outline); paint-order: stroke fill;
  }
  .title-rock { display: block; font-size: 62px; color: var(--rock-yellow); }
  .title-paper { display: block; font-size: 68px; color: var(--paper-white); }
  .title-scissors { display: block; font-size: 76px; color: var(--scissors-mint); }
  .ribbon { position: absolute; left: 150px; top: 300px; width: 440px; height: 70px; }
  .ribbon-text {
    position: absolute; left: 194px; top: 310px; width: 352px; height: 50px;
    display: flex; align-items: center; justify-content: center;
    font-family: "Luckiest Guy", "Bangers", sans-serif; font-size: 32px; color: var(--ribbon-ink); letter-spacing: 1px;
  }
  .details {
    position: absolute; left: 0; right: 0; top: 448px; text-align: center;
    font-family: "Fira Sans Condensed", sans-serif; color: var(--paper-white);
    text-shadow: 0 2px 3px rgba(0,0,0,.45);
  }
  .detail { font-weight: 500; font-size: 22px; line-height: 1.15; }
  .detail strong { font-weight: 700; font-size: 40px; }
  .detail sup { font-size: 20px; }
  .fee { font-size: 28px; font-weight: 700; line-height: 1.2; margin-top: 2px; }
  .heats {
    margin: 10px auto 0; width: 100%; padding: 6px 0;
    background: var(--band-green); color: var(--heats-ink); text-shadow: none;
    font-weight: 800; font-size: 22px; line-height: 1.15;
  }
  .extras {
    margin-top: 10px; font-family: "Bangers", sans-serif; font-size: 24px;
    letter-spacing: 1.5px; line-height: 1.2;
  }
  .contact {
    margin-top: 12px; font-weight: 700; font-size: 17px; line-height: 1.3;
  }
</style>
</head>
<body>
<div class="canvas">
  <article class="flyer">
    <div class="flyer-photo" role="img" aria-label="Photo of two hands playing rock paper scissors, one open as paper and one closed as rock, over a green wheat field under a blue sky"></div>
    <div class="bunting" role="img" aria-label="Colourful party bunting flags strung across the top"></div>

    <div class="club-mark">
      <span class="club-dot"></span>
      <span>Belmoray Sports Center</span>
    </div>
    <div class="county-seal" role="img" aria-label="County seal"></div>

    <h1 class="title">
      <span class="title-rock">Rock</span>
      <span class="title-paper">Paper</span>
      <span class="title-scissors">Scissors</span>
    </h1>
    <svg class="ribbon" viewBox="0 0 440 70" aria-hidden="true">
      <polygon points="0,22 52,22 52,62 0,62 16,42" fill="var(--ribbon-blue)"/>
      <polygon points="440,22 388,22 388,62 440,62 424,42" fill="var(--ribbon-blue)"/>
      <rect x="44" y="10" width="352" height="50" fill="var(--paper-white)" stroke="var(--ribbon-blue)" stroke-width="4"/>
    </svg>
    <div class="ribbon-text">CHAMPIONSHIP</div>

    <section class="details">
      <p class="detail">Date: <strong>June 9<sup>th</sup></strong>, 2018</p>
      <p class="detail">Time: <strong>11<sup>am</sup>-4<sup>pm</sup></strong></p>
      <p class="fee">Fee: $2 to enter, free for spectators</p>
      <p class="heats">Heats to determine the overall<br>‘Rock, Paper, Scissors’ champion!</p>
      <p class="extras">★ Cash prizes on offer &nbsp;★ Live music.<br>★ Food and beverage available for purchase</p>
      <p class="contact">Belmoray Sports Center, Roselle NJ<br>908-555-0163 &nbsp;|&nbsp; www.belmoraypark.example</p>
    </section>
  </article>
</div>
</body>
</html>
```